Create a Brochure Design for Brantley Homecare

Brantley Homecare is a subsidiary of the Brantley Care Group. This brochure is specifically for the Brantley Homecare company and brand. Create a 3 panel, A4, front and back, tri-fold brochure. This brochure will be a way to introduce our Homecare services to the community, prospective clients, and various referral partners. The brochure must be eye catching, unique in its deliverables and demonstrate both attention to detail and comfort. Our organization is sophisticated and built around warmth, care and individualized personal attention. The most important aspect of this design is to focus on creating a nurturing, warm, and inviting feel where you would want to have a Nurse or Nurse’s Aide in your own home or a loved one’s home.

I am open to the creativity of the designer to develop something based on the above criteria; however I would like the design to work well with the existing collateral material. What I mean by that is that while I want everything to have its own personality and stand out as its own brand representative, I still need to be able to tell that the overall design concept stays stylistically inside of the same ‘family’ of existing designed material. Because of this, below I would like for the designer to pull inspiration from the link to our website (Located below) as well as from the attachment of our recently refreshed business cards (Attached). This should allow each design to be unique and creative, while still staying inside of a framework and the feel/style that I am looking for.

Finally, I want all the designers to understand that this brochure design is for a private, in home, healthcare company where we are responsible for providing personalized care for a culturally and ethnically diverse make-up clientele of all ages. The photos that are used must represent an image of warmth, care, and a positive interaction between client and caregiver.

Look under the Brantley Homecare tab at www.brantleycaregroup-example.net

Industry/Entity Type

Healthcare

Requirements
Must have
• • The Brantley Homecare company logo must be included.

```html
<!DOCTYPE html>
<html lang="en">
<head>
<meta charset="UTF-8">
<title>Brantley Homecare – Tri-fold Brochure</title>
<link href="https://fonts.googleapis.com/css2?family=Open+Sans:wght@600;700&display=swap" rel="stylesheet">
<style>
  :root {
    --peach: #f9c58f;
    --peach-shade: #f2b97f;
    --green: #1d7a5b;
    --coral: #ef8f7c;
    --white: #ffffff;
    --paper: #eef0f3;
    --paper-shade: #dfe2e6;
    --stage: #ffffff;
    --skin-light: #e8c9a8;
    --skin-mid: #c99470;
    --skin-deep: #9c6a4c;
    --room-light: #f7f5ee;
    --room-cream: #efe6c9;
    --room-grey: #c9ccc6;
    --mint: #bfe3cf;
    --mint-deep: #8fc7ab;
  }
  * { box-sizing: border-box; margin: 0; padding: 0; }
  html, body {
    width: 1200px; height: 800px; overflow: hidden;
    background: var(--stage);
    font-family: "Open Sans", Verdana, sans-serif;
  }
  .brochure {
    position: absolute; left: 90px; top: 40px;
    width: 1020px; height: 720px;
    display: flex;
    box-shadow: 0 14px 34px rgba(0,0,0,0.2);
  }
  .panel { width: 340px; height: 100%; position: relative; overflow: hidden; }
  .panel + .panel { box-shadow: inset 6px 0 8px -6px rgba(0,0,0,0.18); }

  /* Brand lockup: name set in text with a plain square beside it */
  .brand { display: flex; flex-direction: column; align-items: center; }
  .brand-row { display: flex; align-items: center; gap: 10px; }
  .brand-mark {
    width: 30px; height: 30px; border-radius: 5px;
    background: var(--coral); flex: none;
  }
  .brand-name {
    color: var(--green); font-weight: 700; font-size: 26px;
    line-height: 1.1; white-space: nowrap; letter-spacing: -0.3px;
  }
  .brand-tagline {
    color: var(--green); font-weight: 600; font-size: 11px;
    text-align: center; margin-top: 8px; line-height: 1.3;
  }

  /* Photo areas */
  .photo { position: absolute; }

  /* Panel 1 – contact */
  .panel--contact { background: var(--peach); }
  .panel--contact .brand { position: absolute; top: 82px; left: 0; right: 0; }
  .contact {
    position: absolute; top: 222px; right: 70px;
    color: var(--white); font-style: normal;
    font-weight: 700; font-size: 17px; line-height: 1.3; text-align: right;
  }
  .contact-photo {
    left: 30px; right: 30px; top: 402px; height: 196px;
    background:
      radial-gradient(ellipse 30% 40% at 22% 30%, #f3d36a 0%, rgba(243,211,106,0) 70%),
      radial-gradient(ellipse 40% 55% at 42% 70%, #f4ecc4 0%, rgba(244,236,196,0) 75%),
      radial-gradient(ellipse 30% 60% at 75% 60%, var(--white) 0%, rgba(255,255,255,0) 75%),
      linear-gradient(180deg, var(--room-light) 0%, var(--room-cream) 60%, var(--room-grey) 100%);
    box-shadow: 0 6px 10px rgba(0,0,0,0.18);
  }

  /* Panel 2 – intro */
  .panel--intro { background: linear-gradient(180deg, var(--paper) 0%, var(--paper) 70%, var(--paper-shade) 100%); }
  .site-url {
    position: absolute; top: 24px; left: 0; right: 0; text-align: center;
    color: var(--green); font-weight: 700; font-size: 13px;
  }
  .intro-photo {
    top: 58px; left: 0; right: 0; height: 390px;
    background:
      radial-gradient(ellipse 45% 35% at 30% 35%, var(--skin-light) 0%, rgba(232,201,168,0) 75%),
      radial-gradient(ellipse 55% 40% at 65% 70%, var(--skin-mid) 0%, rgba(201,148,112,0) 75%),
      radial-gradient(ellipse 35% 30% at 50% 55%, var(--skin-deep) 0%, rgba(156,106,76,0) 75%),
      linear-gradient(180deg, #f6f4f1 0%, #e7ddd2 100%);
  }
  .intro-text {
    position: absolute; top: 478px; left: 34px; right: 34px;
    color: var(--green); font-weight: 700; font-size: 15px;
    line-height: 1.4; text-align: justify;
  }

  /* Panel 3 – cover */
  .panel--cover { background: var(--peach); }
  .cover-photo {
    top: 0; left: 0; right: 0; height: 455px;
    background:
      radial-gradient(ellipse 45% 55% at 30% 55%, var(--white) 0%, rgba(255,255,255,0) 75%),
      radial-gradient(ellipse 45% 55% at 75% 75%, var(--mint) 0%, rgba(191,227,207,0) 80%),
      radial-gradient(ellipse 25% 25% at 55% 85%, var(--skin-mid) 0%, rgba(201,148,112,0) 80%),
      linear-gradient(160deg, #f1f4ee 0%, #dfeae2 55%, var(--mint-deep) 100%);
  }
  .cover-brand { position: absolute; top: 528px; left: 0; right: 0; }
  .cover-brand .brand-name { font-size: 28px; }
  .cover-brand .brand-mark { width: 34px; height: 34px; }
</style>
</head>
<body>
  <main class="brochure">
    <section class="panel panel--contact">
      <div class="brand">
        <div class="brand-row">
          <div class="brand-mark"></div>
          <div class="brand-name">Brantley Homecare</div>
        </div>
        <p class="brand-tagline">Someone you can depend on...<br>Without question.</p>
      </div>
      <address class="contact">
        Tel 808-555-0142<br>
        Fax 808-555-0187<br>
        450 Lanakila Ave.<br>
        Suite #310<br>
        Honolulu, HI 96801
      </address>
      <div class="photo contact-photo" role="img" aria-label="Photo of a caregiver in scrubs with a stethoscope sitting beside a smiling elderly woman in a bright room with flowers"></div>
    </section>

    <section class="panel panel--intro">
      <p class="site-url">www.brantleycaregroup-example.net</p>
      <div class="photo intro-photo" role="img" aria-label="Close-up photo of a caregiver's hand gently holding an elderly woman's hand wearing rings"></div>
      <p class="intro-text">Brantley Homecare is licensed by the State of Hawaii as a home healthcare agency. We comply with standards that promote quality healthcare delivery. The delivery of outstanding services to our clients is our top priority.</p>
    </section>

    <section class="panel panel--cover">
      <div class="photo cover-photo" role="img" aria-label="Photo of a smiling young caregiver beside an elderly woman in a mint cardigan holding a walking cane"></div>
      <div class="brand cover-brand">
        <div class="brand-row">
          <div class="brand-mark"></div>
          <div class="brand-name">Brantley Homecare</div>
        </div>
        <p class="brand-tagline">Someone you can depend on...<br>Without question.</p>
      </div>
    </section>
  </main>
</body>
</html>
```